GHollis Busisness Card

I am an aerospace consultant and at this time only need business cards.

Industry/Entity Type

Business

Contact Information for Business Card

Hollis Partners,LLC
Gerald T. Hollis

348 Birch Hollow Road
Madison AL 35762

256-555-0148 (cell)
256-555-0173 (fax)

geraldhollis@mailbrook.net

```html
<!DOCTYPE html>
<html lang="en">
<head>
<meta charset="utf-8">
<title>GHollis Business Card</title>
<link rel="stylesheet" href="https://fonts.googleapis.com/css2?family=Tinos:ital,wght@0,400;0,700;1,400&family=Didact+Gothic&display=swap">
<style>
  :root {
    --backdrop: #c9c6c1;
    --sky: #00adef;
    --night: #032530;
    --emblem-area: #2c6f86;
    --ink: #0c1a20;
    --white: #ffffff;
  }
  html, body {
    margin: 0;
    padding: 0;
    width: 1200px;
    height: 1200px;
    overflow: hidden;
    background: var(--backdrop);
  }
  .card {
    position: absolute;
    left: 75px;
    top: 300px;
    width: 1050px;
    height: 600px;
    box-shadow: 0 6px 18px rgba(0,0,0,0.18);
    overflow: hidden;
  }
  .card-field {
    position: absolute;
    inset: 0;
    width: 100%;
    height: 100%;
  }
  .contact-block {
    position: absolute;
    right: 50px;
    top: 40px;
    width: 520px;
    color: var(--ink);
    font-family: "Tinos", "Times New Roman", serif;
    text-align: right;
  }
  .contact-name {
    margin: 0;
    font-size: 42px;
    font-weight: 700;
    line-height: 1.05;
  }
  .contact-title {
    margin: 0;
    font-size: 27px;
    font-style: italic;
    line-height: 1.2;
  }
  .contact-details {
    list-style: none;
    margin: 48px 0 0 0;
    padding: 0;
    font-size: 29px;
    line-height: 1.4;
  }
  .contact-details li::before {
    content: "\2022";
  }
  .contact-details .continued::before {
    content: "";
  }
  .company-name {
    position: absolute;
    left: 20px;
    top: 370px;
    width: 420px;
    margin: 0;
    color: var(--white);
    font-family: "Didact Gothic", "Helvetica", sans-serif;
    font-weight: 400;
    font-size: 46px;
    line-height: 1.15;
    text-align: center;
  }
</style>
</head>
<body>
  <div class="card">
    <svg class="card-field" viewBox="0 0 1050 600">
      <rect class="sky-panel" x="0" y="0" width="1050" height="600" fill="var(--sky)"/>
      <polygon class="night-panel" points="0,0 410,0 545,600 0,600" fill="var(--night)"/>
      <rect class="emblem-area" x="360" y="200" width="220" height="120" rx="10"
            fill="var(--emblem-area)" role="img"
            aria-label="Company emblem placed on the divide between the blue and dark panels"/>
    </svg>

    <div class="contact-block">
      <h1 class="contact-name">Gerald T. Hollis</h1>
      <p class="contact-title">Aerospace Consultant</p>
      <ul class="contact-details">
        <li>348 Birch Hollow Road Madison</li>
        <li class="continued">AL 35762 256-555-0148</li>
        <li>256-555-0173</li>
        <li>geraldhollis@mailbrook.net</li>
      </ul>
    </div>

    <p class="company-name">Hollis Partners,<br>LLC</p>
  </div>
</body>
</html>
```